Managed IT service provider needs a flyer for small companies

We need a flyer for an MSP company in east Texas called Steadfast Network Partners. We manage small to medium companies IT needs, ranging from cybersecurity, business phones, Anti-virus software, and file management. We would like to see designs using blue and orange. The final design should convey companies need for protection against cyber criminals that use ransomware and upload viruses that can cost these companies hundreds of thousands of dollars.

```html
<!DOCTYPE html>
<html lang="en">
<head>
<meta charset="utf-8">
<title>Steadfast Network Partners – Managed IT Flyer</title>
<link rel="stylesheet" href="https://fonts.googleapis.com/css2?family=Jost:wght@300;400;700;800&display=swap">
<style>
  :root{
    --blue:#1e9ad8;
    --blue-deep:#0f4f9e;
    --blue-band:#1a62b2;
    --footer-blue:#1467b1;
    --orange:#f7931e;
    --ink:#111418;
    --paper-top:#e4e5e7;
    --paper-bottom:#f6f6f6;
    --white:#ffffff;
    --badge:#d9dce1;
  }
  *{margin:0;padding:0;box-sizing:border-box}
  html,body{width:914px;height:1200px;overflow:hidden;background:var(--white)}
  .flyer{position:relative;width:914px;height:1200px;font-family:"Jost",sans-serif;color:var(--ink);
    background:linear-gradient(160deg,var(--paper-top) 0%,var(--paper-bottom) 45%,#e2e3e5 100%);overflow:hidden}
  .hero-art{position:absolute;left:0;top:0;width:914px;height:624px}
  .brand{position:absolute;left:48px;top:70px;display:flex;align-items:center;gap:12px}
  .brand-dot{width:34px;height:34px;border-radius:50%;background:var(--blue)}
  .brand-name{font-weight:700;font-size:25px;line-height:1.05;color:var(--blue);width:230px}
  .headline{position:absolute;left:48px;top:230px;font-weight:800;font-size:36px;line-height:42px;text-transform:uppercase;letter-spacing:.3px}
  .headline .blue{color:var(--blue)}
  .headline .orange{color:var(--orange)}
  .intro{position:absolute;left:48px;top:414px;width:340px;font-weight:300;font-size:14px;line-height:17px}
  .did-you-know{position:absolute;left:48px;top:494px;font-weight:800;font-size:24px;letter-spacing:.4px}
  .stat{position:absolute;top:534px;font-weight:400;font-size:13px;line-height:17px}
  .stat .figure{display:inline-block;background:var(--orange);color:var(--ink);font-weight:400;font-size:25px;line-height:28px;padding:0 4px;margin-right:3px;vertical-align:-2px;clip-path:polygon(0 0,100% 0,92% 100%,0 100%)}
  .stat-1{left:48px}.stat-2{left:312px}.stat-3{left:606px}
  .services{position:absolute;left:0;top:624px;width:914px;height:322px;color:var(--white);
    background:radial-gradient(ellipse at 70% 60%,#2b7fd0 0%,var(--blue-band) 45%,var(--blue-deep) 100%)}
  .services-title{position:absolute;top:22px;width:100%;text-align:center;font-weight:800;font-size:34px;letter-spacing:.5px}
  .services-intro{position:absolute;top:82px;width:100%;text-align:center;font-weight:300;font-size:12.5px;line-height:17px}
  .service{position:absolute;display:flex;align-items:center;gap:22px;font-weight:800;font-size:18px;letter-spacing:.3px}
  .service svg{width:52px;height:48px;flex:none}
  .svc-1{left:190px;top:152px}.svc-2{left:474px;top:152px}
  .svc-3{left:190px;top:242px}.svc-4{left:474px;top:242px}
  .partners{position:absolute;left:0;top:946px;width:914px;height:151px;background:var(--white)}
  .partner-row{position:absolute;width:100%;display:flex;justify-content:center;gap:22px}
  .partner-row.top{top:26px}.partner-row.bottom{top:92px}
  .badge{height:34px;width:72px;border-radius:6px;background:var(--badge)}
  .contact{position:absolute;left:0;top:1097px;width:914px;height:63px;background:var(--footer-blue);color:var(--white);
    display:flex;align-items:center;justify-content:center;gap:50px;font-weight:300;font-size:27px}
  .contact-item{display:flex;align-items:center;gap:12px}
  .contact-item svg{width:24px;height:24px}
</style>
</head>
<body>
<main class="flyer">

  <svg class="hero-art" viewBox="0 0 914 624" aria-hidden="false">
    <defs>
      <linearGradient id="photoTone" x1="0" y1="0" x2="1" y2="1">
        <stop offset="0" stop-color="#3a3f8a"/>
        <stop offset=".45" stop-color="#1a1f3c"/>
        <stop offset="1" stop-color="#2a4e9a"/>
      </linearGradient>
    </defs>
    <path d="M614 0 C545 55 495 125 460 200 C505 125 560 60 640 0 Z" fill="var(--orange)"/>
    <path d="M790 0 C560 100 420 260 447 380 C475 500 650 530 914 478 L914 490 C640 545 462 510 436 382 C410 255 545 95 768 0 Z" fill="var(--blue)"/>
    <path d="M720 0 C560 90 440 250 466 370 C492 470 600 505 720 490 C800 480 870 465 914 450 L914 0 Z" fill="url(#photoTone)" role="img" aria-label="Photo: hooded man in glasses using a smartphone in a dark studio with blue smoke"/>
  </svg>

  <div class="brand">
    <span class="brand-dot"></span>
    <span class="brand-name">Steadfast Network Partners</span>
  </div>

  <h1 class="headline">
    <span class="blue">Providing<br>Protection</span><br>
    <span class="orange">Against Cyber<br>Criminals</span>
  </h1>

  <p class="intro">Providing Security Solution to Companies from ransomware and viruses that can cost these companies hundreds of thousands of dollars</p>

  <h2 class="did-you-know">DID YOU KNOW ?</h2>

  <p class="stat stat-1"><span class="figure">1in5</span> Small businesses will<br>suffer a cyber breach this year</p>
  <p class="stat stat-2"><span class="figure">81%</span> of all breaches happen<br>to small and medium sized businesses.</p>
  <p class="stat stat-3"><span class="figure">97%</span> of breaches could have been<br>prevented with today’s technology.</p>

  <section class="services">
    <h2 class="services-title">MANAGED IT SERVICES</h2>
    <p class="services-intro">Steadfast Network Partners eliminates IT headaches while maximizing efficiency and security.<br>We provide expert IT support and proactive services that improve workflow and increase business uptime.</p>

    <div class="service svc-1">
      <svg viewBox="0 0 52 48" fill="none" stroke="#fff" stroke-width="2">
        <rect x="2" y="2" width="48" height="34" rx="2"/><rect x="6" y="6" width="40" height="24"/>
        <path d="M20 42h12M26 36v6"/>
        <path d="M26 9l8 3v6c0 5-4 8-8 10-4-2-8-5-8-10v-6z" stroke="var(--orange)"/>
      </svg>
      <span>CYBERSECURITY</span>
    </div>
    <div class="service svc-2">
      <svg viewBox="0 0 52 48" fill="none" stroke="#fff" stroke-width="2">
        <rect x="2" y="2" width="48" height="32" rx="2"/><path d="M2 28h48M16 40h20"/>
        <ellipse cx="26" cy="16" rx="5" ry="7" stroke="var(--orange)"/>
        <path d="M19 12h-4M33 12h4M19 20h-4M33 20h4M24 8l-2-3M28 8l2-3" stroke="var(--orange)"/>
      </svg>
      <span>ANTI-VIRUS SOFTWARE</span>
    </div>
    <div class="service svc-3">
      <svg viewBox="0 0 52 48" fill="none" stroke="#fff" stroke-width="2">
        <rect x="8" y="2" width="10" height="44" rx="2"/><rect x="18" y="8" width="22" height="38" rx="2"/>
        <rect x="24" y="14" width="10" height="8" stroke="var(--orange)"/>
        <path d="M24 28h2M29 28h2M34 28h0M24 33h2M29 33h2M24 38h2M29 38h2"/>
      </svg>
      <span>BUSINESS PHONES</span>
    </div>
    <div class="service svc-4">
      <svg viewBox="0 0 52 48" fill="none" stroke="#fff" stroke-width="2">
        <path d="M10 8v38h30" stroke="var(--orange)"/>
        <path d="M14 2h22l8 8v32H14z"/><path d="M20 14h18M20 20h18M20 26h18M20 32h18"/>
      </svg>
      <span>FILE MANAGEMENT</span>
    </div>
  </section>

  <section class="partners" aria-label="Partner badges">
    <div class="partner-row top">
      <span class="badge"></span><span class="badge"></span><span class="badge"></span><span class="badge"></span><span class="badge"></span>
    </div>
    <div class="partner-row bottom">
      <span class="badge"></span><span class="badge"></span><span class="badge"></span>
    </div>
  </section>

  <footer class="contact">
    <span class="contact-item">
      <svg viewBox="0 0 24 24" fill="none" stroke="#fff" stroke-width="1.6"><circle cx="12" cy="12" r="10"/><circle cx="12" cy="12" r="5"/><path d="M7 12h10M12 7v10"/></svg>
      steadfastnetpartners.com
    </span>
    <span class="contact-item">
      <svg viewBox="0 0 24 24" fill="none" stroke="#fff" stroke-width="1.6"><circle cx="12" cy="12" r="10"/><path d="M8.5 7.5l2 2-1.2 1.5c.8 1.5 2 2.7 3.5 3.5l1.5-1.2 2 2-1.5 1.5c-3-.3-7.5-4.8-7.8-7.8z"/></svg>
      (555) 014-2287
    </span>
  </footer>

</main>
</body>
</html>
```